Signage. Will be for store front. Building is on a corner lot. Lots of traffic.

Opening a new location for our landscape business with a garden store (boutique theme) which will have big pottery pots, house plants, ferns and orchids for sale.

And on the side lot of the store we will have bigger bulk items(contractors theme) landscape plants, sod, mulch, soil, rock for sale.

Sign is about 8’x6’

Target Market(s)

Home owners
Landscapers
Builders

Industry/Entity Type

Landscaping

Font styles to use
Sans Serif

Colors
9bcb3c

Requirements
Must have
• “ Installation and Delivery” is a big deal to let people know we do that
Nice to have
• Added a first rendition idea but don’t love it
Added a file with some words to play with
Need help with the words
Should not have
• ?

```html
<!DOCTYPE html>
<html lang="en">
<head>
<meta charset="utf-8">
<title>Fernfield Grove – Garden Center Sign</title>
<link rel="stylesheet" href="https://fonts.googleapis.com/css2?family=Fredoka:wght@500;600&display=swap">
<style>
  :root {
    --page: #f2f2f2;
    --ink: #2b2b2b;
    --deep-green: #467a0c;
    --bright-green: #7cb51e;
    --pale-green: #b8d99a;
    --glow: #f4f9ee;
    --gold: #f7c600;
    --white: #ffffff;
    --olive: #7fa04a;
  }
  html, body {
    margin: 0;
    width: 1200px;
    height: 994px;
    overflow: hidden;
    background: var(--page);
  }
  .sign {
    position: absolute;
    left: 0;
    top: 46px;
    width: 1200px;
    height: 902px;
    overflow: hidden;
    font-family: "Fredoka", "Arial Rounded MT Bold", sans-serif;
  }
  .sign__backdrop {
    position: absolute;
    inset: 0;
  }
  .brand {
    position: absolute;
    left: 170px;
    top: 58px;
    width: 740px;
    text-align: center;
    font-weight: 600;
    font-size: 84px;
    line-height: 92px;
    color: var(--ink);
    letter-spacing: 2px;
  }
  .brand__dot {
    position: absolute;
    left: 935px;
    top: 100px;
    width: 100px;
    height: 100px;
    border-radius: 50%;
    background: var(--olive);
  }
  .headline {
    position: absolute;
    left: 0;
    width: 1200px;
    top: 322px;
    text-align: center;
    font-weight: 600;
    font-size: 132px;
    line-height: 140px;
    color: var(--ink);
    margin: 0;
  }
  .services {
    position: absolute;
    left: 0;
    width: 1200px;
    text-align: center;
    font-weight: 600;
    font-size: 72px;
    line-height: 78px;
    color: var(--gold);
    -webkit-text-stroke: 5px var(--ink);
    paint-order: stroke fill;
    margin: 0;
    white-space: nowrap;
  }
  .services--main { top: 468px; }
  .services--sod { top: 552px; }
  .services__divider {
    display: inline-block;
    width: 4px;
    height: 70px;
    margin: 0 10px;
    vertical-align: -12px;
    background: var(--ink);
  }
  .tagline {
    position: absolute;
    left: 0;
    width: 1200px;
    top: 786px;
    text-align: center;
    font-weight: 600;
    font-size: 82px;
    line-height: 90px;
    color: var(--white);
    margin: 0;
    letter-spacing: 1px;
    white-space: nowrap;
  }
</style>
</head>
<body>
  <section class="sign">
    <svg class="sign__backdrop" width="1200" height="902" viewBox="0 0 1200 902">
      <defs>
        <radialGradient id="panelGlow" cx="0.55" cy="0.62" r="0.65">
          <stop offset="0" stop-color="var(--glow)"/>
          <stop offset="0.55" stop-color="#d6eac4"/>
          <stop offset="1" stop-color="var(--pale-green)"/>
        </radialGradient>
        <linearGradient id="waveGreen" x1="0" y1="0" x2="1" y2="0">
          <stop offset="0" stop-color="var(--deep-green)"/>
          <stop offset="1" stop-color="var(--bright-green)"/>
        </linearGradient>
        <linearGradient id="whiteBand" x1="0" y1="0" x2="1" y2="0">
          <stop offset="0" stop-color="#ffffff"/>
          <stop offset="0.6" stop-color="#dcdcdc"/>
          <stop offset="1" stop-color="#ffffff"/>
        </linearGradient>
        <radialGradient id="foliageFade" cx="0.5" cy="0.5" r="0.5">
          <stop offset="0" stop-color="#8aa85a" stop-opacity="0.22"/>
          <stop offset="1" stop-color="#8aa85a" stop-opacity="0"/>
        </radialGradient>
      </defs>
      <rect class="wave-base" width="1200" height="902" fill="url(#waveGreen)"/>
      <path class="base-band" d="M0,660 C300,770 820,790 1200,600 L1200,902 L0,902 Z" fill="var(--ink)"/>
      <path class="gold-stripe" d="M0,595 C300,705 820,725 1200,485" fill="none" stroke="var(--gold)" stroke-width="22"/>
      <path class="white-stripe" d="M-40,515 C300,650 820,690 1200,445" fill="none" stroke="url(#whiteBand)" stroke-width="62"/>
      <path class="light-panel" d="M150,0 C60,250 150,600 430,672 C720,742 1000,620 1200,430 L1200,0 Z" fill="url(#panelGlow)"/>
      <ellipse class="foliage-art" cx="1110" cy="460" rx="150" ry="460" fill="url(#foliageFade)" role="img" aria-label="Faint line drawing of tropical palm and monstera leaves"/>
    </svg>

    <div class="brand">FERNFIELD<br>GROVE</div>
    <div class="brand__dot"></div>

    <h1 class="headline">GARDEN CENTER</h1>
    <p class="services services--main">LAWN<span class="services__divider"></span>LANDSCAPE<span class="services__divider"></span>NURSERY</p>
    <p class="services services--sod">SOD</p>

    <p class="tagline">INSTALLATION AND DELIVERY</p>
  </section>
</body>
</html>
```